Business Card Design

I am a vocalist and songwriter. I am an alternative soul singer, but there are definitely some jazz elements as well. It would probably be easiest to go to my website to get an idea about my design needs.
www.marisolwhitfield.com
I would like to continue the theme on the first page in the green dress and orchard.
I am not sure if double sided is necessary. I was thinking a qr code to scan and go to the website would be nice. I am not sure if it's necessary.
The font for Quiet Bloom is Rockwell.
Also, I need something else please let me know or you think the QR code is viable, I can upload that as well.
Thanks!
NOTE TO DESIGNERS FROM PH ADMIN:
The business cards for this project should be formatted according to the U.S. template (see links below):
http://storage.pitchhive.com/print_template/vp/pitchhive_usa_businesscard_printready_cmyk_ai.zip
http://storage.pitchhive.com/print_template/vp/pitchhive_usa_businesscard_printready_cmyk_psd.zip
Updates
I have added a psd file which has the logo in it.
I really would like a two sided card with the QR code on the back. That is included in the files
Also, I have included the rockwell font zip file which is the same font used on my website.
Thanks!
Industry/Entity Type
Business
Contact Information for Business Card
Marisol Whitfield
Vocalist/Songwriter
1 (555) 204-6178
info@marisolwhitfield.com
www.marisolwhitfield.com

```html
<!DOCTYPE html>
<html lang="en">
<head>
<meta charset="utf-8">
<title>Marisol Whitfield – Business Card</title>
<link rel="stylesheet" href="https://fonts.googleapis.com/css2?family=Lobster&family=Roboto+Slab:wght@400;600&display=swap">
<style>
  :root {
    --backdrop: #e4e4e4;
    --sky: #cbbca4;
    --haze: #9c8b72;
    --foliage: #4a3e2c;
    --foliage-deep: #2a2419;
    --ink-light: #f4f1ea;
    --accent-red: #e2553c;
    --accent-green: #6cc04a;
    --icon-ink: #2d3a22;
  }
  html, body {
    margin: 0;
    width: 1200px;
    height: 750px;
    overflow: hidden;
    background: var(--backdrop);
  }
  .card {
    position: absolute;
    left: 110px;
    top: 95px;
    width: 980px;
    height: 560px;
    border-radius: 42px;
    overflow: hidden;
    font-family: "Roboto Slab", Georgia, serif;
    color: var(--ink-light);
  }
  .card__photo {
    position: absolute;
    inset: 0;
    background:
      radial-gradient(ellipse at 8% 30%, var(--sky) 0%, rgba(203,188,164,0.6) 25%, transparent 55%),
      linear-gradient(160deg, var(--sky) 0%, var(--haze) 30%, var(--foliage) 55%, var(--foliage-deep) 100%);
  }
  .brand-name {
    position: absolute;
    left: 56px;
    top: 190px;
    margin: 0;
    font-weight: 600;
    font-size: 54px;
    line-height: 1.05;
    color: var(--ink-light);
  }
  .title-block {
    position: absolute;
    left: 510px;
    top: 80px;
    text-align: center;
  }
  .title-block__name {
    margin: 0;
    font-family: "Lobster", cursive;
    font-weight: 400;
    font-size: 54px;
    color: var(--accent-red);
  }
  .title-block__role {
    margin: 0;
    font-size: 22px;
    color: var(--accent-green);
    letter-spacing: 0.5px;
  }
  .icon {
    position: absolute;
    width: 50px;
    height: 50px;
  }
  .icon--phone { left: 470px; top: 250px; }
  .icon--web { left: 840px; top: 235px; }
  .icon--mail { left: 380px; top: 395px; }
  .contact {
    position: absolute;
    margin: 0;
    font-size: 22px;
    color: var(--ink-light);
    white-space: nowrap;
  }
  .contact--phone { left: 430px; top: 322px; }
  .contact--web { left: 640px; top: 322px; }
  .contact--mail { left: 60px; top: 475px; }
</style>
</head>
<body>
  <article class="card">
    <div class="card__photo" role="img" aria-label="Sepia photograph of an apple orchard with leafy branches against a pale sky"></div>

    <h1 class="brand-name">Marisol<br>Whitfield</h1>

    <header class="title-block">
      <h2 class="title-block__name">Marisol Whitfield</h2>
      <p class="title-block__role">Vocalist/Songwriter</p>
    </header>

    <svg class="icon icon--phone" viewBox="0 0 50 50" aria-hidden="true">
      <circle cx="25" cy="25" r="22" fill="none" stroke="var(--accent-green)" stroke-width="3"/>
      <path d="M17 14 l5 0 l2 7 l-3 2 q3 6 9 9 l2 -3 l7 2 l0 5 q-1 2 -4 2 q-20 -3 -20 -20 q0 -3 2 -4 z" fill="var(--accent-green)"/>
    </svg>

    <svg class="icon icon--web" viewBox="0 0 50 50" aria-hidden="true">
      <circle cx="25" cy="25" r="24" fill="var(--accent-green)"/>
      <path d="M18 12 L34 28 L26 28 L30 37 L27 38 L23 29 L18 34 Z" fill="var(--icon-ink)"/>
    </svg>

    <svg class="icon icon--mail" viewBox="0 0 50 50" aria-hidden="true">
      <circle cx="25" cy="25" r="24" fill="var(--accent-green)"/>
      <rect x="12" y="16" width="26" height="18" fill="none" stroke="var(--icon-ink)" stroke-width="2.5"/>
      <path d="M12 16 L25 27 L38 16" fill="none" stroke="var(--icon-ink)" stroke-width="2.5"/>
    </svg>

    <p class="contact contact--phone">1 (555) 204-6178</p>
    <p class="contact contact--web">www.marisolwhitfield.com</p>
    <p class="contact contact--mail">info@marisolwhitfield.com</p>
  </article>
</body>
</html>
```